Hip surgeon needs a educative book cover design

I need to re-design my old book cover for its 3rd edition.
It's a small book dedicated to my patients, who underwent total hip replacement. It's meant to help people getting around the basic care after a total hip replacement surgery and getting back to their normal, active life.
The title is: "Bright mornings: a walking companion guide".
I already had a new logo, new stationery and new website design from PixelHarbor (please see the attachments).
The final design should be look alike the other fresh new designs. It must communicate health, peacefulness.
I also attached the manual as it looks today for reference.
A5 size.
Just cover and back cover.

```html
<!DOCTYPE html>
<html lang="en">
<head>
<meta charset="utf-8">
<title>Bright mornings: a walking companion guide</title>
<link rel="stylesheet" href="https://fonts.googleapis.com/css2?family=Roboto:wght@300;400;500&display=swap">
<style>
  :root {
    --blue-deep: #5a8fca;
    --blue-soft: #a8c3e3;
    --blue-band: #2f7cbf;
    --pink-soft: #f3dbe8;
    --sky-pale: #cfe4f4;
    --ink: #111a24;
    --white: #ffffff;
  }
  html, body {
    margin: 0;
    padding: 0;
    overflow: hidden;
    background: #ffffff;
  }
  .cover {
    position: relative;
    width: 826px;
    height: 1200px;
    overflow: hidden;
    background: var(--blue-soft);
    font-family: "Roboto", Arial, sans-serif;
  }
  .cover__column {
    position: absolute;
    left: 0;
    top: 0;
    width: 239px;
    height: 564px;
    background: var(--blue-deep);
  }
  .cover__accent {
    position: absolute;
    left: 0;
    top: 564px;
    width: 239px;
    height: 410px;
    background: linear-gradient(180deg, var(--pink-soft) 0%, #e9e3ef 45%, var(--sky-pale) 100%);
  }
  .cover__image {
    position: absolute;
    left: 239px;
    top: 500px;
    width: 587px;
    height: 474px;
    background: linear-gradient(180deg, #a8c3e3 0%, #4f8aa6 18%, #1d4b57 45%, #2c5a3e 70%, #a9a83a 100%);
  }
  .cover__title {
    position: absolute;
    left: 49px;
    top: 360px;
    margin: 0;
    color: var(--ink);
    font-weight: 400;
    line-height: 1.15;
  }
  .cover__title-main {
    display: block;
    font-size: 50px;
    letter-spacing: -0.5px;
  }
  .cover__title-sub {
    display: block;
    font-size: 44px;
    font-weight: 300;
    letter-spacing: -0.3px;
  }
  .cover__footer {
    position: absolute;
    left: 0;
    top: 974px;
    width: 826px;
    height: 226px;
    background: var(--blue-band);
  }
  .author {
    position: absolute;
    left: 52px;
    top: 1000px;
    display: flex;
    align-items: center;
    gap: 20px;
    color: var(--white);
  }
  .author__mark {
    width: 84px;
    height: 84px;
    border-radius: 50%;
    background: var(--white);
    flex: none;
  }
  .author__name {
    margin: 0;
    font-size: 38px;
    font-weight: 400;
    line-height: 1.1;
  }
  .author__role {
    margin: 4px 0 0;
    font-size: 27px;
    font-weight: 400;
  }
</style>
</head>
<body>
  <main class="cover">
    <div class="cover__column"></div>
    <div class="cover__accent"></div>
    <div class="cover__image" role="img" aria-label="X-ray of a pelvis and hip joints in teal and yellow tones"></div>

    <h1 class="cover__title">
      <span class="cover__title-main">Bright mornings:</span>
      <span class="cover__title-sub">a walking companion guide</span>
    </h1>

    <footer class="cover__footer"></footer>
    <div class="author">
      <span class="author__mark" aria-hidden="true"></span>
      <div>
        <p class="author__name">Dr. Lucas M. Ferreira</p>
        <p class="author__role">Cirurgia do Quadril</p>
      </div>
    </div>
  </main>
</body>
</html>
```